Business card for Velora Homeworks

Hi again, I need a business card for my Velora Homeworks business you have been working on with the following information:

Tessa Quill
Director
m. 0438 276 615
e. tessa@velorahomeworks.com.au
w. www.velorahomeworks.com.au

Maybe you could use the original design (using both the green & white) and where the white box is you could include the above details (name / mobile / etc) - Perhaps the 'i' in Tessa could be the bow tie again?

Then the back could be green with black writing stating:

Services Offered:

* Personal Assistant Concierge
* Decluttering Concierge
* Home Management Concierge
* FIFO Concierge
* Events Concierge
* Leisure & Travel Concierge
* Seasonal Concierge
* Professional Concierge

Many thanks
Updates

Hi Everyone I'm really sorry but I am working with just one designer on this brief, thank you for your work and apologies for my error.

Industry/Entity Type

Business

```html
<!DOCTYPE html>
<html lang="en">
<head>
<meta charset="utf-8">
<title>Velora Homeworks – Business Card</title>
<link href="https://fonts.googleapis.com/css2?family=Titillium+Web:wght@300;400&family=Pinyon+Script&display=swap" rel="stylesheet">
<style>
  :root {
    --green: #5f9b32;
    --green-light: #8cc63e;
    --white: #ffffff;
    --ink: #111111;
    --backdrop: #ecebe7;
    --sans: "Titillium Web", "Helvetica Neue", Arial, sans-serif;
    --script: "Pinyon Script", "Brush Script MT", cursive;
  }
  * { box-sizing: border-box; margin: 0; padding: 0; }
  html, body {
    width: 1200px;
    height: 800px;
    overflow: hidden;
    background: var(--backdrop);
  }
  .canvas {
    position: relative;
    width: 1200px;
    height: 800px;
    overflow: hidden;
  }
  .card {
    position: absolute;
    left: 320px;
    width: 560px;
    height: 320px;
    background: var(--green);
    box-shadow: 0 2px 6px rgba(0,0,0,0.18);
    overflow: hidden;
  }
  .card--front { top: 60px; }
  .card--back  { top: 420px; }

  /* Front */
  .front__header {
    position: absolute;
    left: 26px;
    top: 10px;
  }
  .brand-name {
    font-family: var(--sans);
    font-weight: 300;
    color: var(--green-light);
    line-height: 1;
    white-space: nowrap;
  }
  .front__header .brand-name { font-size: 38px; }
  .tagline {
    font-family: var(--script);
    color: var(--ink);
    line-height: 1;
    white-space: nowrap;
  }
  .front__header .tagline {
    font-size: 22px;
    margin: 4px 0 0 30px;
  }
  .front__details {
    position: absolute;
    left: 0;
    top: 96px;
    width: 100%;
    height: 166px;
    background: var(--white);
    text-align: center;
    padding-top: 30px;
  }
  .person-name {
    font-family: var(--sans);
    font-weight: 400;
    font-size: 34px;
    color: var(--green);
    line-height: 1;
  }
  .person-role {
    font-family: var(--script);
    font-size: 30px;
    color: var(--ink);
    line-height: 1.2;
    margin-top: 6px;
  }
  .person-phone {
    font-family: var(--sans);
    font-weight: 400;
    font-size: 24px;
    color: var(--ink);
    line-height: 1;
    margin-top: 2px;
  }
  .front__contact {
    position: absolute;
    right: 18px;
    top: 268px;
    text-align: right;
    font-family: var(--sans);
    font-size: 17px;
    line-height: 22px;
    color: var(--white);
  }

  /* Back */
  .back__brand {
    position: absolute;
    top: 44px;
    left: 0;
    width: 100%;
    text-align: center;
  }
  .back__brand .brand-name { font-size: 54px; }
  .back__brand .tagline {
    font-size: 34px;
    margin-top: 2px;
  }
  .services {
    position: absolute;
    top: 200px;
    left: 0;
    width: 100%;
    list-style: none;
    text-align: center;
    font-family: var(--sans);
    font-size: 19px;
    line-height: 24px;
    color: var(--white);
  }
  .services .sep { margin: 0 8px; }
</style>
</head>
<body>
<main class="canvas">

  <section class="card card--front" aria-label="Business card front">
    <header class="front__header">
      <div class="brand-name">Velora Homeworks</div>
      <div class="tagline">Your Personal Concierge</div>
    </header>
    <div class="front__details">
      <div class="person-name">Tessa Quill</div>
      <div class="person-role">Director</div>
      <div class="person-phone">0438 276 615</div>
    </div>
    <address class="front__contact" style="font-style:normal">
      <div>tessa@velorahomeworks.com.au</div>
      <div>www.velorahomeworks.com.au</div>
    </address>
  </section>

  <section class="card card--back" aria-label="Business card back">
    <div class="back__brand">
      <div class="brand-name">Velora Homeworks</div>
      <div class="tagline">Your Personal Concierge</div>
    </div>
    <ul class="services">
      <li>Personal Assistant Concierge<span class="sep">|</span>Decluttering Concierge</li>
      <li>Home Management Concierge<span class="sep">|</span>FIFO Concierge</li>
      <li>Events Concierge<span class="sep">|</span>Leisure &amp; Travel Concierge</li>
      <li>Seasonal Concierge<span class="sep">|</span>Professional Concierge</li>
    </ul>
  </section>

</main>
</body>
</html>
```